Create modern and sleek business card for luxury real estate company

We're a "boutique" real estate office looking for a design that gets across a highly modern luxury brand. Blacks and whites are probably the best colors unless we try a silver foil for the logo. I've attached a version of our current logo here. I'd like to swap out the current font on there with Gotham Light Regular.

I'm looking to have one side of the card have the logo with the space for our agents info on the other side.

Target Market(s)

Young professionals in a "luxury" headspace

Industry/Entity Type

Real estate

Contact Information for Business Card

A place for agent name, cell number, website. The slogan "Quietly Elevating Every Address".

Font styles to use
Other font styles liked:
• Gotham Regular

Colors

Designer to choose only greyscale colors for use in the design.

Requirements
Must have
• Matte black as the background color. Clean lines and use of contrast. A specific design aspect that will use silver foil.
Nice to have
• Up in the air on integrating a QR code
Should not have
• Any houses or other real estate related design (ex: a clip art house)

```html
<!DOCTYPE html>
<html lang="en">
<head>
<meta charset="utf-8">
<title>Meridian Estates — Business Card</title>
<link href="https://fonts.googleapis.com/css2?family=Montserrat:wght@300;400;600&display=swap" rel="stylesheet">
<style>
  :root {
    --backdrop: #3a3a3b;
    --card-black: #0d0d0e;
    --foil: #d9d9db;
    --foil-dim: #8a8a8d;
    --gloss: #1b1b1d;
    --text-white: #f2f2f2;
    --text-grey: #6f6f72;
  }
  * { margin: 0; padding: 0; box-sizing: border-box; }
  html, body { width: 1200px; height: 801px; overflow: hidden; }
  body {
    background: var(--backdrop);
    font-family: "Montserrat", sans-serif;
    display: flex;
    align-items: center;
    justify-content: center;
    gap: 48px;
  }
  .card {
    position: relative;
    width: 540px;
    height: 308px;
    background: var(--card-black);
    border-radius: 3px;
    box-shadow: 0 18px 40px rgba(0,0,0,.45);
    overflow: hidden;
  }
  .card-front .ghost-circle {
    position: absolute;
    right: -70px;
    top: -80px;
    width: 300px;
    height: 300px;
    border-radius: 50%;
    border: 10px solid var(--gloss);
  }
  .brand {
    position: absolute;
    display: flex;
    align-items: center;
    gap: 12px;
  }
  .brand-mark {
    border-radius: 50%;
    border: 2px solid currentColor;
    flex: none;
  }
  .brand-name {
    font-weight: 400;
    letter-spacing: .14em;
    line-height: 1.15;
    text-transform: uppercase;
  }
  .card-front .brand { left: 34px; top: 36px; color: var(--text-white); }
  .card-front .brand-mark { width: 42px; height: 42px; }
  .card-front .brand-name { font-size: 17px; }
  .agent { position: absolute; left: 34px; top: 118px; }
  .agent-name {
    color: var(--text-white);
    font-weight: 600;
    font-size: 17px;
    letter-spacing: .04em;
    text-transform: uppercase;
  }
  .agent-title { color: var(--text-grey); font-size: 13px; font-weight: 400; margin-top: 2px; }
  .contact-list { list-style: none; margin-top: 14px; }
  .contact-list li {
    display: flex;
    align-items: center;
    gap: 8px;
    color: var(--text-white);
    font-size: 13px;
    font-weight: 400;
    line-height: 1.7;
  }
  .contact-list svg { width: 11px; height: 11px; fill: var(--text-grey); flex: none; }
  .slogan { color: var(--text-white); font-size: 13px; margin-top: 12px; font-weight: 400; }
  .card-back .brand {
    left: 50%;
    top: 50%;
    transform: translate(-50%, -50%);
    gap: 18px;
    color: var(--foil);
  }
  .card-back .brand-mark { width: 84px; height: 84px; border-width: 3px; border-color: var(--foil-dim); }
  .card-back .brand-name {
    font-size: 30px;
    background: linear-gradient(100deg, var(--foil-dim), var(--foil) 45%, var(--foil-dim));
    -webkit-background-clip: text;
    background-clip: text;
    color: transparent;
  }
</style>
</head>
<body>
  <section class="card card-front">
    <div class="ghost-circle"></div>
    <div class="brand">
      <span class="brand-mark"></span>
      <span class="brand-name">Meridian<br>Estates</span>
    </div>
    <div class="agent">
      <p class="agent-name">Daniel Harwick</p>
      <p class="agent-title">President</p>
      <ul class="contact-list">
        <li><svg viewBox="0 0 12 12" aria-hidden="true"><path d="M2.5 1 4.5 3.2 3.6 4.6C4.3 6 5.9 7.6 7.4 8.4L8.8 7.5 11 9.5 9.8 11C5.5 10.8 1.2 6.5 1 2.2Z"/></svg>555-214-0387</li>
        <li><svg viewBox="0 0 12 12" aria-hidden="true"><path d="M1 2.5h10v7H1Zm.8.8L6 6.6l4.2-3.3Z"/></svg>dharwick@meridianestates.com</li>
        <li><svg viewBox="0 0 12 12" aria-hidden="true"><circle cx="6" cy="6" r="5"/></svg>www.meridianestates.com</li>
      </ul>
      <p class="slogan">Quietly Elevating Every Address</p>
    </div>
  </section>
  <section class="card card-back">
    <div class="brand">
      <span class="brand-mark"></span>
      <span class="brand-name">Meridian<br>Estates</span>
    </div>
  </section>
</body>
</html>
```